electrical company van design

we need a design for our new van, we are an electrical contracting business and we need our design to be eye-catching which make people remember our business name and what we do.

Our business colours are Blue and Orange

Target Market(s)

customers looking for an electrician

Font styles to use
Sans Serif

Colors
0493ce
f78f20

Requirements
Must have
• - Logo / Name
- Services
- Phone Number
- QR code to link to our website
- Ampwright Guild logo
- 24/7 Emergency service

```html
<!DOCTYPE html>
<html lang="en">
<head>
<meta charset="utf-8">
<title>Ridgeline Electrical – Van Livery</title>
<link rel="stylesheet" href="https://fonts.googleapis.com/css2?family=Montserrat:ital,wght@0,400;0,500;0,600;0,800;1,800&display=swap">
<style>
  :root {
    --brand-blue: #1a72bb;
    --brand-orange: #e4572e;
    --body-white: #eef0f2;
    --window-grey: #8b8c96;
    --page: #ffffff;
    --ink-dark: #1d2a44;
  }
  html, body { margin: 0; padding: 0; overflow: hidden; background: var(--page); }
  .canvas { width: 1200px; height: 1011px; position: relative; overflow: hidden; background: var(--page); }
  .van-side { position: absolute; left: 0; width: 1200px; height: 470px; }
  .van-side--driver { top: 20px; }
  .van-side--passenger { top: 525px; }
  .van-side text { font-family: "Montserrat", sans-serif; }
  .services-title { font-size: 31px; font-weight: 500; fill: var(--brand-orange); }
  .services-item { font-size: 15px; font-weight: 500; fill: var(--brand-orange); }
  .brand-name { font-size: 60px; font-weight: 800; fill: var(--brand-blue); letter-spacing: -1px; }
  .brand-line { font-size: 22px; font-weight: 600; fill: var(--brand-blue); }
  .brand-sub { font-size: 10px; font-weight: 600; fill: var(--brand-orange); letter-spacing: 4px; }
  .emergency-big { font-size: 36px; font-weight: 800; font-style: italic; fill: var(--brand-orange); }
  .emergency-small { font-size: 21px; font-weight: 800; font-style: italic; fill: var(--brand-orange); }
  .phone { font-size: 52px; font-weight: 800; fill: #ffffff; letter-spacing: 2px; }
  .qr-label { font-size: 14px; font-weight: 800; fill: var(--brand-blue); }
  .guild-name { font-size: 11px; font-weight: 600; fill: var(--ink-dark); }
</style>
</head>
<body>
<div class="canvas">

  <!-- Driver side: front faces left -->
  <svg class="van-side van-side--driver" viewBox="0 0 1200 470" xmlns="http://www.w3.org/2000/svg">
    <rect class="panel-body" x="55" y="20" width="1100" height="400" rx="40" fill="var(--body-white)"/>
    <path class="window" role="img" aria-label="Cab side window" d="M300 80 L530 45 L550 60 L550 175 L310 195 L295 170 Z" fill="var(--window-grey)"/>
    <path class="rear-blue" d="M1018 20 L1125 20 Q1155 20 1155 60 L1155 380 Q1155 420 1115 420 L870 420 L870 360 L1005 185 L950 185 Z" fill="var(--brand-blue)"/>
    <path class="bolt" d="M958 20 L1018 20 L950 185 L1005 185 L905 345 L878 345 L930 212 L873 212 Z" fill="var(--brand-orange)"/>
    <rect class="phone-band" x="330" y="328" width="560" height="64" fill="var(--brand-blue)"/>

    <text class="services-title" x="730" y="95" text-anchor="middle">Our Services:</text>
    <text class="services-item" x="730" y="124" text-anchor="middle">· Lorem ipsum  · Lorem ipsum</text>
    <text class="services-item" x="730" y="143" text-anchor="middle">· Lorem ipsum  · Lorem ipsum</text>

    <circle class="brand-dot" cx="622" cy="235" r="14" fill="var(--brand-orange)"/>
    <text class="brand-name" x="648" y="257">KORVA</text>
    <text class="brand-line" x="717" y="304" text-anchor="middle">RIDGELINE ELECTRICAL</text>
    <text class="brand-sub" x="717" y="320" text-anchor="middle">POWER &amp; CONTROLS</text>

    <text class="emergency-big" x="415" y="250" text-anchor="middle">24/7</text>
    <text class="emergency-small" x="415" y="279" text-anchor="middle">Emergency</text>
    <text class="emergency-small" x="415" y="302" text-anchor="middle">service</text>

    <text class="phone" x="603" y="380" text-anchor="middle">+00123 456 789</text>

    <rect class="qr-box" x="1013" y="66" width="82" height="82" fill="#ffffff"/>
    <text class="qr-label" x="1054" y="104" text-anchor="middle">QR</text>
    <text class="qr-label" x="1054" y="121" text-anchor="middle">CODE</text>

    <rect class="guild-badge" x="990" y="230" width="120" height="43" rx="4" fill="#ffffff"/>
    <rect class="guild-mark" x="998" y="241" width="20" height="20" fill="var(--ink-dark)"/>
    <text class="guild-name" x="1025" y="249">AMPWRIGHT</text>
    <text class="guild-name" x="1025" y="262">GUILD</text>
  </svg>

  <!-- Passenger side: front faces right -->
  <svg class="van-side van-side--passenger" viewBox="0 0 1200 470" xmlns="http://www.w3.org/2000/svg">
    <rect class="panel-body" x="55" y="20" width="1100" height="400" rx="40" fill="var(--body-white)"/>
    <path class="window" role="img" aria-label="Cab side window" d="M910 80 L680 45 L660 60 L660 175 L900 195 L915 170 Z" fill="var(--window-grey)"/>
    <path class="rear-blue" d="M192 20 L85 20 Q55 20 55 60 L55 380 Q55 420 95 420 L340 420 L340 360 L205 185 L260 185 Z" fill="var(--brand-blue)"/>
    <path class="bolt" d="M252 20 L192 20 L260 185 L205 185 L305 345 L332 345 L280 212 L337 212 Z" fill="var(--brand-orange)"/>
    <rect class="phone-band" x="330" y="328" width="520" height="64" fill="var(--brand-blue)"/>

    <text class="services-title" x="475" y="95" text-anchor="middle">Our Services:</text>
    <text class="services-item" x="475" y="124" text-anchor="middle">· Lorem ipsum  · Lorem ipsum</text>
    <text class="services-item" x="475" y="143" text-anchor="middle">· Lorem ipsum  · Lorem ipsum</text>

    <circle class="brand-dot" cx="367" cy="235" r="14" fill="var(--brand-orange)"/>
    <text class="brand-name" x="393" y="257">KORVA</text>
    <text class="brand-line" x="480" y="304" text-anchor="middle">RIDGELINE ELECTRICAL</text>
    <text class="brand-sub" x="480" y="320" text-anchor="middle">POWER &amp; CONTROLS</text>

    <text class="emergency-big" x="785" y="250" text-anchor="middle">24/7</text>
    <text class="emergency-small" x="785" y="279" text-anchor="middle">Emergency</text>
    <text class="emergency-small" x="785" y="302" text-anchor="middle">service</text>

    <text class="phone" x="595" y="380" text-anchor="middle">+00123 456 789</text>

    <rect class="qr-box" x="113" y="66" width="82" height="82" fill="#ffffff"/>
    <text class="qr-label" x="154" y="104" text-anchor="middle">QR</text>
    <text class="qr-label" x="154" y="121" text-anchor="middle">CODE</text>

    <rect class="guild-badge" x="90" y="230" width="120" height="43" rx="4" fill="#ffffff"/>
    <rect class="guild-mark" x="98" y="241" width="20" height="20" fill="var(--ink-dark)"/>
    <text class="guild-name" x="125" y="249">AMPWRIGHT</text>
    <text class="guild-name" x="125" y="262">GUILD</text>
  </svg>

</div>
</body>
</html>
```